business card, letterhead, and envelope design for mobile ultrasound imaging
Corvane Sonography Partners, LLC
Simple
Maren Tocks BS, RDMS, RVT
Managing Partner
6184 County Road 41S
Harlow Bend, FL 32901
P.O. Box 7126
Brackton, FL 32905-5453
marentocks@corvanesono.example
www.corvanesono.example

```html
<!DOCTYPE html>
<html lang="en">
<head>
<meta charset="utf-8">
<title>Corvane Sonography Partners – Stationery</title>
<link rel="stylesheet" href="https://fonts.googleapis.com/css2?family=Marcellus&family=Lato:wght@400;700&display=swap">
<style>
  :root {
    --paper: #ffffff;
    --canvas: #ffffff;
    --navy: #1c3f8a;
    --blue: #2a7fd0;
    --green: #8cc63f;
    --ink: #4a4a4a;
    --rule: #9a9a9a;
    --shadow: rgba(0,0,0,0.28);
  }
  * { box-sizing: border-box; margin: 0; padding: 0; }
  html, body { width: 1200px; height: 482px; overflow: hidden; background: var(--canvas); }
  body { position: relative; font-family: "Lato", sans-serif; color: var(--ink); }

  .sheet {
    position: absolute; background: var(--paper);
    box-shadow: 2px 3px 7px var(--shadow);
    overflow: hidden;
  }
  .fax-sheet { left: 22px; top: 24px; width: 350px; height: 444px; }
  .letterhead { left: 790px; top: 24px; width: 350px; height: 444px; }
  .envelope-front { left: 391px; top: 43px; width: 382px; height: 185px; }
  .envelope-back { left: 391px; top: 259px; width: 382px; height: 185px; }
  .card { left: 1032px; width: 144px; height: 72px; }
  .card-front { top: 312px; }
  .card-back { top: 396px; }

  .swoosh { position: absolute; left: 0; top: 0; width: 100%; }

  .brand { position: absolute; text-align: center; }
  .brand-mark { display: block; margin: 0 auto; border-radius: 50%; background: var(--blue); }
  .brand-name {
    font-family: "Marcellus", serif; color: var(--navy);
    text-transform: uppercase; letter-spacing: 0.04em; line-height: 1.15; font-weight: 400;
  }

  .header-brand { left: 0; right: 0; top: 50px; }
  .header-brand .brand-mark { width: 18px; height: 18px; }
  .header-brand .brand-name { font-size: 9px; margin-top: 4px; }

  .address { text-align: center; font-size: 4.6px; line-height: 1.5; color: var(--ink); }
  .header-address { position: absolute; left: 0; right: 0; top: 94px; }

  .fax-form { position: absolute; left: 34px; right: 34px; top: 152px; font-size: 6px; }
  .fax-row { display: flex; gap: 24px; margin-bottom: 10px; }
  .fax-field { flex: 1; display: flex; align-items: flex-end; gap: 6px; }
  .fax-field span { width: 26px; }
  .fax-field i { flex: 1; border-bottom: 0.6px solid var(--rule); height: 7px; }
  .fax-checks { display: flex; justify-content: space-between; margin-top: 18px; font-size: 5.4px; }
  .fax-checks label { display: flex; align-items: center; gap: 3px; }
  .fax-checks label::before { content: ""; width: 6px; height: 6px; border: 0.6px solid var(--ink); }

  .env-brand { left: 0; right: 0; top: 50px; }
  .env-brand .brand-mark { width: 14px; height: 14px; }
  .env-brand .brand-name { font-size: 7px; margin-top: 3px; }
  .env-address { position: absolute; left: 0; right: 0; top: 82px; font-size: 4.4px; }

  .flap { position: absolute; inset: 0; width: 100%; height: 100%; }
  .back-brand { left: 0; right: 0; top: 98px; }
  .back-brand .brand-mark { width: 14px; height: 14px; }

  .card-brand { left: 8px; top: 20px; width: 60px; }
  .card-brand .brand-mark { width: 9px; height: 9px; }
  .card-brand .brand-name { font-size: 4.2px; margin-top: 2px; }
  .card-contact { position: absolute; right: 6px; top: 20px; width: 68px; text-align: right; font-size: 3.4px; line-height: 1.45; }
  .card-contact strong { font-size: 4.4px; color: var(--navy); display: block; }
  .card-mark { position: absolute; left: 50%; top: 50%; width: 16px; height: 16px; margin: -8px 0 0 -8px; border-radius: 50%; background: var(--blue); }
</style>
</head>
<body>

<section class="sheet fax-sheet">
  <svg class="swoosh" viewBox="0 0 350 50" height="50" preserveAspectRatio="none" aria-hidden="true">
    <path d="M-10 36 Q175 -6 360 36" fill="none" stroke="var(--green)" stroke-width="4"/>
    <path d="M-10 44 Q175 4 360 44" fill="none" stroke="var(--blue)" stroke-width="1.4"/>
  </svg>
  <div class="brand header-brand">
    <span class="brand-mark"></span>
    <p class="brand-name">Corvane Sonography Partners, LLC</p>
  </div>
  <div class="address header-address">
    <p>6184 County Road 41S · Harlow Bend, FL 32901 · P.O. Box 7126 · Brackton, FL 32905-7126</p>
    <p>Tel 850.555.0142 · Fax 850.555.0143 · marentocks@corvanesono.example · www.corvanesono.example</p>
  </div>
  <div class="fax-form">
    <div class="fax-row"><div class="fax-field"><span>To:</span><i></i></div><div class="fax-field"><span>From:</span><i></i></div></div>
    <div class="fax-row"><div class="fax-field"><span>Fax:</span><i></i></div><div class="fax-field"><span>Pages:</span><i></i></div></div>
    <div class="fax-row"><div class="fax-field"><span>Phone:</span><i></i></div><div class="fax-field"><span>Date:</span><i></i></div></div>
    <div class="fax-row"><div class="fax-field"><span>Re:</span><i></i></div><div class="fax-field"><span>CC:</span><i></i></div></div>
    <div class="fax-checks">
      <label>Urgent</label><label>For Review</label><label>Please Comment</label><label>Please Reply</label><label>Please Recycle</label>
    </div>
  </div>
</section>

<section class="sheet envelope-front">
  <svg class="swoosh" viewBox="0 0 382 44" height="44" preserveAspectRatio="none" aria-hidden="true">
    <path d="M-10 32 Q191 -6 392 32" fill="none" stroke="var(--green)" stroke-width="4"/>
    <path d="M-10 40 Q191 4 392 40" fill="none" stroke="var(--blue)" stroke-width="1.4"/>
  </svg>
  <div class="brand env-brand">
    <span class="brand-mark"></span>
    <p class="brand-name">Corvane Sonography Partners, LLC</p>
  </div>
  <p class="address env-address">6184 County Road 41S · Harlow Bend, FL 32901 · P.O. Box 7126 · Brackton, FL 32905-7126</p>
</section>

<section class="sheet envelope-back">
  <svg class="flap" viewBox="0 0 382 185" preserveAspectRatio="none" aria-hidden="true">
    <path d="M0 2 L191 120 L382 2" fill="none" stroke="var(--rule)" stroke-width="0.8"/>
    <path d="M0 185 L150 96 M382 185 L232 96" fill="none" stroke="#cfcfcf" stroke-width="0.6"/>
  </svg>
  <div class="brand back-brand"><span class="brand-mark"></span></div>
</section>

<section class="sheet letterhead">
  <svg class="swoosh" viewBox="0 0 350 50" height="50" preserveAspectRatio="none" aria-hidden="true">
    <path d="M-10 36 Q175 -6 360 36" fill="none" stroke="var(--green)" stroke-width="4"/>
    <path d="M-10 44 Q175 4 360 44" fill="none" stroke="var(--blue)" stroke-width="1.4"/>
  </svg>
  <div class="brand header-brand">
    <span class="brand-mark"></span>
    <p class="brand-name">Corvane Sonography Partners, LLC</p>
  </div>
  <div class="address header-address">
    <p>6184 County Road 41S · Harlow Bend, FL 32901 · P.O. Box 7126 · Brackton, FL 32905-7126</p>
    <p>marentocks@corvanesono.example · www.corvanesono.example</p>
  </div>
</section>

<section class="sheet card card-front">
  <svg class="swoosh" viewBox="0 0 144 16" height="16" preserveAspectRatio="none" aria-hidden="true">
    <path d="M-4 11 Q72 -3 148 11" fill="none" stroke="var(--green)" stroke-width="2"/>
    <path d="M-4 14 Q72 1 148 14" fill="none" stroke="var(--blue)" stroke-width="0.8"/>
  </svg>
  <div class="brand card-brand">
    <span class="brand-mark"></span>
    <p class="brand-name">Corvane Sonography Partners, LLC</p>
  </div>
  <div class="card-contact">
    <strong>Maren Tocks</strong>
    <p>BS, RDMS, RVT · Managing Partner</p>
    <p>6184 County Road 41S</p>
    <p>Harlow Bend, FL 32901</p>
    <p>marentocks@corvanesono.example</p>
    <p>www.corvanesono.example</p>
  </div>
</section>

<section class="sheet card card-back">
  <span class="card-mark"></span>
</section>

</body>
</html>
```